Design a visually appealing layout for our company mission and values. I want to create a visually appealing 1 page flyer that presents our company mission and values to clients as well as to our internal team/staff. We will utilize the 1 page flyer in internal and external presentations about our company. We will also use the flyer in sales proposals/marketing packages.

Target Market(s)

Internal team members as well as external prospective clients, existing clients & referral partners

Industry/Entity Type

Financial Service

Colors

Designer to choose colors to be used in the design.

Requirements
Must have
• Should reflect our company brand so I have included our Pantone panel, fonts etc. I have provided our company logo as well which should be part of the branded document
Nice to have
• I would like the presentation to be useable in different formats and to different audiences so something that is more graphic/visual heavy - otherwise it's a lot of words that people don't read.
• Would like to be able to easily include in our corporate template powerpoint presentation.

```html
<!DOCTYPE html>
<html lang="en">
<head>
<meta charset="UTF-8">
<title>Mission &amp; Values</title>
<link href="https://fonts.googleapis.com/css2?family=Cinzel:wght@700;900&family=Montserrat:wght@400;500;600;700&display=swap" rel="stylesheet">
<style>
  :root {
    --brand-blue: #2a7db6;
    --brand-green: #8cc152;
    --brand-grey: #a7a9ac;
    --line-grey: #b9bcc0;
    --ink: #2b2b2b;
    --body-ink: #333333;
    --tagline-ink: #6d6e71;
    --page: #ffffff;
    --backdrop: #d9d9d9;
  }
  * { box-sizing: border-box; margin: 0; padding: 0; }
  html, body { width: 703px; height: 1200px; overflow: hidden; background: var(--backdrop); }
  .flyer {
    position: relative;
    width: 703px; height: 1200px;
    background:
      linear-gradient(135deg, rgba(255,255,255,0) 40%, rgba(207,226,245,0.55) 70%, rgba(230,240,250,0.3) 100%),
      var(--page);
    font-family: "Montserrat", sans-serif;
    color: var(--ink);
    overflow: hidden;
  }
  .brand {
    position: absolute; top: 70px; left: 0; width: 100%;
    text-align: center;
  }
  .brand-name {
    display: inline-flex; align-items: center; gap: 12px;
    font-weight: 600; font-size: 30px; line-height: 36px; color: var(--brand-blue);
    letter-spacing: 0.5px;
  }
  .brand-dot { width: 18px; height: 18px; border-radius: 50%; background: var(--brand-green); }
  .brand-tagline {
    margin-top: 22px;
    font-size: 12px; font-weight: 500; letter-spacing: 3px;
    color: var(--tagline-ink); text-transform: uppercase;
  }
  .page-title {
    position: absolute; top: 230px; left: 0; width: 100%;
    text-align: center; line-height: 56px;
    font-family: "Cinzel", serif; font-weight: 900; font-size: 44px;
    letter-spacing: 0.5px;
  }
  .page-title .mission { color: var(--brand-blue); }
  .page-title .amp { color: var(--brand-grey); }
  .page-title .values { color: var(--brand-green); }
  .title-rule {
    position: absolute; top: 294px; left: 106px; width: 492px; height: 1px;
    background: var(--brand-blue);
  }
  .title-rule::after {
    content: ""; position: absolute; left: 232px; top: -2px; width: 28px; height: 4px;
    background: var(--brand-blue);
  }
  .section-label {
    position: absolute; left: 0; width: 100%;
    display: flex; justify-content: center; align-items: flex-end; gap: 4px;
    font-weight: 700; font-size: 25px; line-height: 30px; color: var(--brand-green); letter-spacing: 1px;
  }
  .section-label .dash {
    width: 48px; height: 6px; margin-bottom: 5px;
    border-top: 1px solid var(--brand-blue); border-bottom: 1px solid var(--brand-blue);
  }
  .section-label.mission-label { top: 348px; }
  .section-label.value-label { top: 457px; }
  .mission-statement {
    position: absolute; top: 397px; left: 0; width: 100%;
    text-align: center; font-weight: 600; font-size: 14.5px; color: var(--ink);
  }
  .timeline-line {
    position: absolute; left: 203px; top: 539px; width: 1px; height: 491px;
    background: var(--line-grey);
  }
  .value {
    position: absolute; left: 0; width: 100%; height: 130px;
  }
  .value-badge { position: absolute; left: 52px; top: 0; width: 120px; height: 130px; }
  .value-node {
    position: absolute; left: 196px; top: 58px; width: 15px; height: 15px;
    border-radius: 50%; border: 1.5px solid var(--brand-grey); background: var(--page);
  }
  .value-node::after {
    content: ""; position: absolute; left: 3px; top: 3px; width: 6px; height: 6px;
    border-radius: 50%; background: var(--brand-green);
  }
  .value-text { position: absolute; left: 237px; top: 54px; width: 420px; }
  .value-name { font-weight: 700; font-size: 17px; color: var(--ink); margin-bottom: 9px; letter-spacing: 0.3px; }
  .value-desc { font-size: 13.6px; line-height: 1.22; color: var(--body-ink); }
  .value.teamwork { top: 474px; }
  .value.empowerment { top: 636px; }
  .value.knowledge { top: 797px; }
  .value.proactivity { top: 965px; }
  .value.teamwork .value-text { top: 50px; }
  .website {
    position: absolute; top: 1134px; left: 0; width: 100%;
    display: flex; justify-content: center; align-items: center; gap: 8px;
    font-weight: 700; font-size: 16px; color: var(--ink);
  }
  .website .dash { width: 46px; height: 5px; border-top: 1px solid var(--brand-blue); border-bottom: 1px solid var(--brand-blue); }
  .website .domain { color: var(--brand-green); }
  .footer-band { position: absolute; left: 0; bottom: 0; width: 703px; height: 30px; }
</style>
</head>
<body>
<main class="flyer">
  <header class="brand">
    <div class="brand-name"><span class="brand-dot"></span>Larkvale Pension Group</div>
    <p class="brand-tagline">Guide the way. Build a steady future.</p>
  </header>

  <h1 class="page-title"><span class="mission">MISSION</span> <span class="amp">&amp;</span> <span class="values">VALUES</span></h1>
  <div class="title-rule"></div>

  <h2 class="section-label mission-label"><span class="dash"></span>OUR MISSION<span class="dash"></span></h2>
  <p class="mission-statement">To proactively support organizations and lead them toward a secure future</p>

  <h2 class="section-label value-label"><span class="dash"></span>WE VALUE<span class="dash"></span></h2>

  <div class="timeline-line"></div>

  <section class="value teamwork">
    <svg class="value-badge" viewBox="0 0 120 130">
      <path d="M60 9 A56 56 0 0 1 60 121" fill="none" stroke="var(--line-grey)" stroke-width="1.5"/>
      <circle cx="60" cy="9" r="3.5" fill="#fff" stroke="var(--brand-grey)"/>
      <circle cx="60" cy="121" r="3.5" fill="#fff" stroke="var(--brand-grey)"/>
      <path d="M60 17 A48 48 0 0 1 60 113 L60 99 A34 34 0 0 0 60 31 Z" fill="#c4c6c9"/>
      <circle cx="60" cy="65" r="37" fill="none" stroke="var(--brand-green)" stroke-width="6"/>
      <circle cx="60" cy="65" r="30" fill="var(--brand-blue)" stroke="#fff" stroke-width="3" role="img" aria-label="Teamwork icon: group of people"/>
      <polygon points="110,59 118,65 110,71" fill="var(--brand-green)"/>
    </svg>
    <span class="value-node"></span>
    <div class="value-text">
      <h3 class="value-name">Teamwork</h3>
      <p class="value-desc">Collaborating with team members, clients and partners to maintain a high level of communication, accountability and engagement to achieve our common goals</p>
    </div>
  </section>

  <section class="value empowerment">
    <svg class="value-badge" viewBox="0 0 120 130">
      <path d="M60 9 A56 56 0 0 1 60 121" fill="none" stroke="var(--line-grey)" stroke-width="1.5"/>
      <circle cx="60" cy="9" r="3.5" fill="#fff" stroke="var(--brand-grey)"/>
      <circle cx="60" cy="121" r="3.5" fill="#fff" stroke="var(--brand-grey)"/>
      <path d="M60 17 A48 48 0 0 1 60 113 L60 99 A34 34 0 0 0 60 31 Z" fill="#c4c6c9"/>
      <circle cx="60" cy="65" r="37" fill="none" stroke="var(--brand-green)" stroke-width="6"/>
      <circle cx="60" cy="65" r="30" fill="var(--brand-blue)" stroke="#fff" stroke-width="3" role="img" aria-label="Financial empowerment icon: shield with arrows"/>
      <polygon points="110,59 118,65 110,71" fill="var(--brand-green)"/>
    </svg>
    <span class="value-node"></span>
    <div class="value-text">
      <h3 class="value-name">Financial Empowerment</h3>
      <p class="value-desc">We commit ourselves to providing the best retirement solutions to guide our clients toward financial freedom</p>
    </div>
  </section>

  <section class="value knowledge">
    <svg class="value-badge" viewBox="0 0 120 130">
      <path d="M60 9 A56 56 0 0 1 60 121" fill="none" stroke="var(--line-grey)" stroke-width="1.5"/>
      <circle cx="60" cy="9" r="3.5" fill="#fff" stroke="var(--brand-grey)"/>
      <circle cx="60" cy="121" r="3.5" fill="#fff" stroke="var(--brand-grey)"/>
      <path d="M60 17 A48 48 0 0 1 60 113 L60 99 A34 34 0 0 0 60 31 Z" fill="#c4c6c9"/>
      <circle cx="60" cy="65" r="37" fill="none" stroke="var(--brand-green)" stroke-width="6"/>
      <circle cx="60" cy="65" r="30" fill="var(--brand-blue)" stroke="#fff" stroke-width="3" role="img" aria-label="Knowledge icon: head with ideas"/>
      <polygon points="110,59 118,65 110,71" fill="var(--brand-green)"/>
    </svg>
    <span class="value-node"></span>
    <div class="value-text">
      <h3 class="value-name">Knowledge</h3>
      <p class="value-desc">Our team of highly trained and credentialed experts work to educate and lead our clients toward success</p>
    </div>
  </section>

  <section class="value proactivity">
    <svg class="value-badge" viewBox="0 0 120 130">
      <path d="M60 9 A56 56 0 0 1 60 121" fill="none" stroke="var(--line-grey)" stroke-width="1.5"/>
      <circle cx="60" cy="9" r="3.5" fill="#fff" stroke="var(--brand-grey)"/>
      <circle cx="60" cy="121" r="3.5" fill="#fff" stroke="var(--brand-grey)"/>
      <path d="M60 17 A48 48 0 0 1 60 113 L60 99 A34 34 0 0 0 60 31 Z" fill="#c4c6c9"/>
      <circle cx="60" cy="65" r="37" fill="none" stroke="var(--brand-green)" stroke-width="6"/>
      <circle cx="60" cy="65" r="30" fill="var(--brand-blue)" stroke="#fff" stroke-width="3" role="img" aria-label="Proactivity icon: person with outward arrows"/>
      <polygon points="110,59 118,65 110,71" fill="var(--brand-green)"/>
    </svg>
    <span class="value-node"></span>
    <div class="value-text">
      <h3 class="value-name">Proactivity</h3>
      <p class="value-desc">We hold ourselves accountable in anticipating regulatory changes and keeping you and your plan in compliance</p>
    </div>
  </section>

  <p class="website"><span class="dash"></span><span class="url">www.<span class="domain">larkvalepension</span>.com</span><span class="dash"></span></p>

  <svg class="footer-band" viewBox="0 0 703 30" preserveAspectRatio="none">
    <path d="M0 4 L190 4 L210 16 L520 16 L540 4 L703 4 L703 30 L0 30 Z" fill="var(--brand-blue)"/>
    <path d="M196 6 L212 16 L518 16 L534 6 L530 6 L516 13 L214 13 L200 6 Z" fill="var(--brand-grey)"/>
  </svg>
</main>
</body>
</html>
```